Labels for probiotic care products as Body Cream, Shower gel, Hand soap, ....

We are a starting a business in Flanders Belgium. We are looking for a label for care products, based on probiotics or good bacterie. We are looking for a fresh design that attracts people who wants a good product, based on naturally components. The products make that the microflora of the skin becomes and remains natural. The label must we be adaptive on bottles of 15 cm height to 8 cm height and a width of 4,5 cm. The brand name is KOLA EMU (beautiful skin in Hawaiian) or maybe just KOLA.

Industry/Entity Type

Business

Colors

Designer to choose colors to be used in the design.

Requirements
Must have
• somewhere the text "Probiotic Skin Care"
• I also have to tell that the bottles are white.
Nice to have
• I uploaded the 9 existing labels, but I want a totally new one, because the labels of our cleaning products are the same. I also uploaded a mood bord of labels I like.

```html
<!DOCTYPE html>
<html lang="en">
<head>
<meta charset="utf-8">
<title>KOLA EMU – Body Cream Label</title>
<link rel="stylesheet" href="https://fonts.googleapis.com/css2?family=Open+Sans:wght@700;800&family=Oswald:wght@600;700&display=swap">
<style>
  :root {
    --green-deep: #7cbf3a;
    --green-top: #8dc63f;
    --green-band: #a8d15a;
    --green-frame: #c9e39a;
    --green-paper: #f4f9e8;
    --green-stripe: #9ccc5a;
    --circle-green: #3f9a4a;
    --skin-light: #fbd9bd;
    --skin-edge: #f5852a;
    --ink-dark: #1d2a12;
    --white: #ffffff;
  }
  html, body {
    margin: 0;
    padding: 0;
    width: 1200px;
    height: 3536px;
    overflow: hidden;
    background: var(--white);
  }
  .label {
    position: relative;
    width: 1200px;
    height: 3536px;
  }
  .label-art {
    position: absolute;
    inset: 0;
  }
  .brand-name {
    position: absolute;
    top: 160px;
    left: 0;
    width: 1200px;
    text-align: center;
    font-family: "Open Sans", Arial, sans-serif;
    font-weight: 800;
    font-size: 112px;
    letter-spacing: 2px;
    color: var(--white);
    line-height: 1;
  }
  .product-title {
    position: absolute;
    top: 1300px;
    left: 0;
    width: 1200px;
    text-align: center;
    font-family: "Oswald", "Arial Narrow", sans-serif;
    font-weight: 700;
    font-size: 200px;
    line-height: 0.92;
    color: var(--white);
    text-shadow: 0 0 6px rgba(0, 60, 20, 0.35);
  }
  .product-claim {
    position: absolute;
    top: 1716px;
    left: 0;
    width: 1200px;
    text-align: center;
    font-family: "Oswald", "Arial Narrow", sans-serif;
    font-weight: 600;
    font-size: 40px;
    line-height: 1.2;
    color: var(--white);
  }
  .range-line {
    position: absolute;
    top: 3382px;
    left: 0;
    width: 1200px;
    text-align: center;
    font-family: "Open Sans", Arial, sans-serif;
    font-weight: 800;
    font-size: 50px;
    color: var(--ink-dark);
    line-height: 1;
  }
</style>
</head>
<body>
<div class="label">
  <svg class="label-art" width="1200" height="3536" viewBox="0 0 1200 3536" xmlns="http://www.w3.org/2000/svg">
    <defs>
      <clipPath id="label-shape">
        <path d="M40 3480 Q40 3536 96 3536 L1104 3536 Q1160 3536 1160 3480 L1160 420 Q1160 150 1010 60 Q900 0 600 0 Q300 0 190 60 Q40 150 40 420 Z"/>
      </clipPath>
      <pattern id="stripe-lines" width="1200" height="12" patternUnits="userSpaceOnUse">
        <rect width="1200" height="3" fill="var(--green-stripe)"/>
      </pattern>
      <radialGradient id="skin-tone" cx="50%" cy="50%" r="60%">
        <stop offset="0%" stop-color="var(--skin-light)"/>
        <stop offset="80%" stop-color="#f9c89e"/>
        <stop offset="100%" stop-color="var(--skin-edge)"/>
      </radialGradient>
      <radialGradient id="circle-fill" cx="50%" cy="50%" r="50%">
        <stop offset="0%" stop-color="var(--circle-green)" stop-opacity="0.85"/>
        <stop offset="85%" stop-color="var(--circle-green)" stop-opacity="0.7"/>
        <stop offset="100%" stop-color="#6dbb5c" stop-opacity="0.55"/>
      </radialGradient>
    </defs>

    <g clip-path="url(#label-shape)">
      <rect class="label-frame" width="1200" height="3536" fill="var(--green-frame)"/>
      <rect class="label-paper" x="72" y="300" width="1056" height="2900" fill="var(--green-paper)"/>
      <rect class="label-stripes" x="72" y="300" width="1056" height="2900" fill="url(#stripe-lines)"/>
      <rect class="top-band" x="0" y="0" width="1200" height="330" fill="var(--green-top)"/>
      <rect class="bottom-band" x="0" y="3230" width="1200" height="306" fill="var(--green-band)"/>
    </g>

    <rect class="figure-area" x="290" y="520" width="620" height="2900" rx="240"
          fill="url(#skin-tone)" stroke="var(--skin-edge)" stroke-width="10"
          role="img" aria-label="Illustration of a standing human body silhouette in peach with an orange outline"/>

    <circle class="title-circle-glow" cx="600" cy="1580" r="478" fill="none" stroke="#b9e0a6" stroke-width="16" opacity="0.8"/>
    <circle class="title-circle" cx="600" cy="1580" r="464" fill="url(#circle-fill)"/>
  </svg>

  <div class="brand-name">KOLA EMU</div>
  <div class="product-title">BODY<br>CREAM</div>
  <div class="product-claim">ensuring that the<br>microflora of the skin<br>becomes and remains natural</div>
  <div class="range-line">PROBIOTIC SKIN CARE</div>
</div>
</body>
</html>
```